Vesk Architecture

We are a architectural design and build company working between scales 1/1000 to 1/1 we want people to understand our difference from our design experience and quality.we build hotels restourants and office spaces.Our company name is Vesk architecture to mind sustainability.

We want to write our adress phone and work spesifications on the card and we want our logo as backround.

Ps:you could find the logo adress and phone box numbers from the web:www.veskmimarlik-ornek.com

Target Market(s)

Who looks for experts.

Industry/Entity Type

Architecture

Requirements
Must have
• Design is over everything.
Should not have
• we don want it to be colorfull

```html
<!DOCTYPE html>
<html lang="en">
<head>
<meta charset="utf-8">
<title>Vesk Architecture – Business Card</title>
<link rel="stylesheet" href="https://fonts.googleapis.com/css2?family=Arimo:wght@400&display=swap">
<style>
  :root {
    --page: #f2f2f2;
    --card: #ffffff;
    --ink: #111111;
    --ghost: #c4c4c4;
    --edge: #1a1a1a;
  }
  * { margin: 0; padding: 0; box-sizing: border-box; }
  html, body {
    width: 1200px;
    height: 1200px;
    overflow: hidden;
    background: var(--page);
  }
  .canvas {
    width: 1200px;
    height: 1200px;
    display: flex;
    align-items: center;
    justify-content: center;
  }
  .business-card {
    position: relative;
    width: 900px;
    height: 560px;
    background: var(--card);
    border: 2px solid var(--edge);
    overflow: hidden;
    font-family: "Arimo", "Helvetica Neue", Arial, sans-serif;
    color: var(--ink);
  }
  .backdrop-name {
    position: absolute;
    left: 70px;
    top: 20px;
    font-size: 380px;
    line-height: 1;
    letter-spacing: -6px;
    color: var(--ghost);
    white-space: nowrap;
  }
  .backdrop-sub {
    position: absolute;
    left: 150px;
    bottom: 32px;
    font-size: 64px;
    letter-spacing: 10px;
    color: var(--ghost);
  }
  .brand-name {
    position: absolute;
    top: 36px;
    left: 0;
    width: 100%;
    text-align: center;
    line-height: 1;
  }
  .brand-name .word {
    display: block;
    font-size: 52px;
    letter-spacing: -1px;
  }
  .brand-name .sub {
    display: block;
    font-size: 12px;
    letter-spacing: 3px;
    margin-top: 4px;
  }
  .contact {
    position: absolute;
    top: 140px;
    left: 0;
    width: 100%;
    text-align: center;
    font-size: 33px;
    line-height: 1.3;
    font-style: normal;
  }
</style>
</head>
<body>
  <main class="canvas">
    <section class="business-card">
      <div class="backdrop-name" aria-hidden="true">vesk</div>
      <div class="backdrop-sub" aria-hidden="true">MİMARLIK</div>

      <h1 class="brand-name">
        <span class="word">vesk</span>
        <span class="sub">MİMARLIK</span>
      </h1>

      <address class="contact">
        Yelken Mah. Liman Cad. Defne Sok.<br>
        No: 48 Kiyi Merkez/Istanbul<br>
        T. 0216 555 01 47<br>
        F. 0216 555 01 48<br>
        E. info@veskmimarlik-ornek.com
      </address>
    </section>
  </main>
</body>
</html>
```